Stationery Required - Own Logo provided

Hi,

We are a retail company called 'Copperfinch Trading Limited' based in the UK and would like some corporate stationery designed.

We have provided our Logo which we would like to use (Its attached to this brief)...

The designs must be orginal, professional, stylish and interesting!

Target Market(s)

We will use this stationery to communicate with our wholesale suppliers and employees, so it must have a 'professional' feel about it.

Industry/Entity Type

It Company

Requirements
Must have
• Must be professional, corporate, stylish and not to 'fussy'. we require ... Business card design, a4 letter, compliment slip. All designs must be supplied in a format where the text (address/telephone numbers etc..) can be edited, as we have alot of staff and operate out of several different premises.
Nice to have
• I would like a windows backround picture file supplied as well so we can integrate that onto our computer systems.

```html
<!DOCTYPE html>
<html lang="en">
<head>
<meta charset="utf-8">
<title>Copperfinch Trading Limited – Stationery</title>
<link href="https://fonts.googleapis.com/css2?family=Ubuntu:wght@500&family=Open+Sans:wght@400;600&display=swap" rel="stylesheet">
<style>
  :root {
    --backdrop: #58585a;
    --paper: #ffffff;
    --green-light: #8dc21f;
    --green-dark: #3f5a17;
    --text-grey: #6b6b6b;
    --rule: #9cc83a;
  }
  * { box-sizing: border-box; margin: 0; padding: 0; }
  html, body { width: 1200px; height: 1006px; overflow: hidden; }
  body {
    background: var(--backdrop);
    position: relative;
    font-family: "Open Sans", Arial, sans-serif;
    color: var(--text-grey);
  }
  .sheet { position: absolute; background: var(--paper); overflow: hidden; }

  .brand {
    position: absolute;
    display: flex;
    align-items: center;
    gap: 6px;
    font-family: "Ubuntu", Arial, sans-serif;
    font-weight: 500;
    color: var(--green-dark);
    white-space: nowrap;
  }
  .brand-square { background: var(--green-light); flex: none; }
  .brand-mark {
    position: absolute;
    background: linear-gradient(135deg, var(--green-light), var(--green-dark));
  }

  .contact { position: absolute; font-size: 7px; line-height: 11px; white-space: nowrap; }
  .rule { position: absolute; width: 1px; background: var(--rule); }

  /* business card front */
  .card-front {
    left: 64px; top: 62px; width: 230px; height: 132px;
    border-radius: 8px 0 0 0;
    background: linear-gradient(180deg, #86b71c 0%, #5a8419 55%, #3b5812 100%);
  }
  .card-front .brand { right: 16px; top: 82px; font-size: 11px; gap: 5px; color: #ffffff; }
  .card-front .brand-square { width: 8px; height: 8px; background: #ffffff; }

  /* business card back */
  .card-back { left: 304px; top: 62px; width: 226px; height: 132px; border-radius: 0 8px 0 0; }
  .card-back .brand { left: 12px; top: 50px; font-size: 7.5px; gap: 4px; }
  .card-back .brand-square { width: 6px; height: 6px; }
  .person { position: absolute; right: 14px; top: 44px; text-align: right; }
  .person-name { font-size: 8px; font-weight: 600; color: #333; }
  .person-role { font-size: 5.5px; color: var(--green-light); }
  .card-back .contact { font-size: 6px; line-height: 9px; top: 92px; }
  .card-back .address { left: 12px; }
  .card-back .phone { right: 14px; text-align: right; }

  /* letterhead */
  .letterhead { left: 62px; top: 210px; width: 528px; height: 746px; }
  .letterhead .brand { left: 0; right: 0; justify-content: center; top: 30px; font-size: 15px; }
  .letterhead .brand-square { width: 12px; height: 12px; }
  .letterhead .rule { top: 690px; height: 46px; }
  .letterhead .contact { top: 700px; }
  .letterhead .brand-mark { left: 374px; top: 680px; width: 60px; height: 58px; }

  /* compliment slip */
  .slip { left: 610px; top: 70px; width: 528px; height: 248px; }
  .slip .brand { left: 46px; top: 24px; font-size: 8.5px; gap: 4px; }
  .slip .brand-square { width: 7px; height: 7px; }
  .slip .rule { top: 10px; height: 42px; }
  .slip .contact { top: 14px; font-size: 6.5px; line-height: 10px; }
  .slip .brand-mark { left: 450px; top: 190px; width: 46px; height: 46px; }
</style>
</head>
<body>

<section class="sheet card-front" aria-label="Business card front">
  <div class="brand"><span class="brand-square"></span>Copperfinch Trading Limited</div>
</section>

<section class="sheet card-back" aria-label="Business card back">
  <div class="brand"><span class="brand-square"></span>Copperfinch Trading Limited</div>
  <div class="person">
    <p class="person-name">Martin Hale</p>
    <p class="person-role">Company Director</p>
  </div>
  <div class="contact address">17 Mill Lane, Ashcombe,<br>Ashfordshire AB12 3CD</div>
  <div class="contact phone">07700 900123<br>hello@copperfinch.example</div>
</section>

<section class="sheet letterhead" aria-label="A4 letterhead">
  <div class="brand"><span class="brand-square"></span>Copperfinch Trading Limited</div>
  <span class="rule" style="left:14px"></span>
  <div class="contact" style="left:22px">17 Mill Lane, Ashcombe,<br>Ashfordshire AB12 3CD</div>
  <span class="rule" style="left:150px"></span>
  <div class="contact" style="left:160px">07700 900123<br>hello@copperfinch.example</div>
  <span class="rule" style="left:290px"></span>
  <div class="brand-mark" aria-hidden="true"></div>
</section>

<section class="sheet slip" aria-label="Compliment slip">
  <div class="brand"><span class="brand-square"></span>Copperfinch Trading Limited</div>
  <span class="rule" style="left:200px"></span>
  <div class="contact" style="left:208px">17 Mill Lane, Ashcombe,<br>Ashfordshire AB12 3CD</div>
  <span class="rule" style="left:344px"></span>
  <div class="contact" style="left:352px">07700 900123<br>hello@copperfinch.example</div>
  <div class="brand-mark" aria-hidden="true"></div>
</section>

</body>
</html>
```